BrambleWorks business card

Looking for business card design that supports our company/software values. We have 2 logo designs at the moment but open to change if you think you can enhance the brand. Check out website www.brambleworks.com.au.

Target Market(s)

Education

Contact Information for Business Card

Name, title, mobile, email and website

Font styles to use
Sans Serif

Colors

Designer to choose colors to be used in the design.

Requirements
Must have
• BrambleWorks logo with tree and tagline on rear side with dark grey background colour

```html
<!DOCTYPE html>
<html lang="en">
<head>
<meta charset="utf-8">
<title>BrambleWorks Business Card</title>
<link href="https://fonts.googleapis.com/css2?family=Lato:wght@400;700&display=swap" rel="stylesheet">
<style>
  :root {
    --stage: #3b3431;
    --card: #141414;
    --card-back: #1a1a1a;
    --pattern: #242424;
    --white: #f2f2f2;
    --grey: #9a9a9a;
    --rule: #555555;
    --green: #5fc32a;
  }
  * { margin: 0; padding: 0; box-sizing: border-box; }
  html, body {
    width: 1200px; height: 844px; overflow: hidden;
    background: var(--stage);
    font-family: "Lato", sans-serif;
  }
  .cards {
    position: absolute; inset: 0;
    display: flex; align-items: center; justify-content: center; gap: 40px;
  }
  .card {
    position: relative;
    width: 540px; height: 309px;
    box-shadow: 0 10px 30px rgba(0,0,0,.45);
  }
  .card-front { background: var(--card); color: var(--white); }
  .card-back { background: var(--card-back); }

  .brand { position: absolute; left: 40px; top: 52px; display: flex; align-items: center; gap: 16px; }
  .brand-dot { width: 62px; height: 62px; border-radius: 50%; background: var(--green); flex: none; }
  .brand-name { font-size: 38px; font-weight: 400; color: var(--white); line-height: 1; white-space: nowrap; }
  .brand-rule { height: 1px; background: var(--white); margin: 8px 0 6px; }
  .brand-tagline { font-size: 15px; color: var(--white); letter-spacing: .3px; white-space: nowrap; }

  .divider { position: absolute; left: 270px; top: 160px; width: 1px; height: 70px; background: var(--rule); }

  .person { position: absolute; right: 290px; top: 185px; text-align: right; white-space: nowrap; }
  .person-name { font-size: 17px; font-weight: 700; color: var(--green); text-transform: uppercase; letter-spacing: .3px; }
  .person-title { font-size: 14px; color: var(--grey); margin-top: 2px; }

  .contacts { position: absolute; left: 290px; top: 160px; list-style: none; }
  .contacts li { display: flex; align-items: center; gap: 8px; font-size: 14px; color: var(--grey); line-height: 22px; white-space: nowrap; }
  .contacts svg { width: 11px; height: 11px; fill: var(--green); flex: none; }
  .contacts .icon-mail path { fill: none; stroke: var(--card); stroke-width: 1.2; }

  .address { position: absolute; left: 40px; bottom: 30px; font-size: 14px; color: var(--grey); white-space: nowrap; }

  .back-pattern { position: absolute; inset: 0; background: linear-gradient(135deg, var(--pattern), var(--card-back) 60%, var(--pattern)); }
  .back-brand { position: absolute; right: 40px; top: 118px; display: flex; align-items: center; gap: 8px; }
  .back-brand .brand-dot { width: 22px; height: 22px; }
  .back-brand .brand-name { font-size: 16px; }
</style>
</head>
<body>
<main class="cards">
  <section class="card card-front" aria-label="Card front">
    <div class="brand">
      <span class="brand-dot"></span>
      <div>
        <div class="brand-name">BrambleWorks</div>
        <div class="brand-rule"></div>
        <div class="brand-tagline">Student Success Platform</div>
      </div>
    </div>

    <div class="person">
      <div class="person-name">Daniel Hart</div>
      <div class="person-title">Managing Director</div>
    </div>

    <div class="divider"></div>

    <ul class="contacts">
      <li>
        <svg viewBox="0 0 12 12"><path d="M2 1h2.5l1 3-1.5 1a6 6 0 0 0 3 3l1-1.5 3 1V10a1 1 0 0 1-1 1A9 9 0 0 1 1 2a1 1 0 0 1 1-1z"/></svg>
        061-908 372 514
      </li>
      <li>
        <svg class="icon-mail" viewBox="0 0 12 12"><rect x="1" y="2.5" width="10" height="7" rx="0.8"/><path d="M1.5 3l4.5 3.5L10.5 3"/></svg>
        info@brambleworks.com.au
      </li>
      <li>
        <svg viewBox="0 0 12 12"><circle cx="6" cy="6" r="5.5"/></svg>
        www.brambleworks.com.au
      </li>
    </ul>

    <div class="address">18 Fernhill Road, Suite 3, 30217, Australia</div>
  </section>

  <section class="card card-back" aria-label="Card back">
    <div class="back-pattern" role="img" aria-label="Faint repeating brand pattern across the dark background"></div>
    <div class="back-brand">
      <span class="brand-dot"></span>
      <span class="brand-name">BrambleWorks</span>
    </div>
  </section>
</main>
</body>
</html>
```